Architectural firm needs a graphic representation of our Master Planning process

We need an image to convey our 3-phase, 8-step Master Planning process that we utilize when designing plans for schools K-12. What we currently use looks very outdated in both the design and color scheme. We'd like an EPS created that can be scaled without distortion. The files I've attached show the current graphic and an instruction sheet which also contains our colors.

```html
<!DOCTYPE html>
<html lang="en">
<head>
<meta charset="utf-8">
<title>Master Planning Process</title>
<link href="https://fonts.googleapis.com/css2?family=Poppins:wght@300;400;500;600;700&display=swap" rel="stylesheet">
<style>
  :root {
    --school: #22c0c8;
    --school-bright: #00e5ff;
    --arch: #a8002f;
    --arch-dot: #d6003c;
    --arch-band: #d9505a;
    --fund: #66d622;
    --fund-bright: #b5f51a;
    --node: #b3b3b3;
    --ink: #5a5a5a;
    --title: #cfcfcf;
    --paper: #ffffff;
  }
  html, body {
    margin: 0;
    padding: 0;
    width: 1200px;
    height: 1200px;
    overflow: hidden;
    background: var(--paper);
  }
  .process-chart {
    display: block;
    width: 1200px;
    height: 1200px;
    font-family: "Poppins", sans-serif;
  }
  .title { font-size: 38px; font-weight: 400; fill: var(--title); letter-spacing: 1px; }
  .role-label { font-size: 19px; font-weight: 600; letter-spacing: 1px; }
  .role-school { fill: var(--school); }
  .role-arch { fill: var(--arch); }
  .role-fund { fill: var(--fund); }
  .step-label { font-size: 19px; font-weight: 600; fill: var(--ink); letter-spacing: 1.2px; }
  .step-label.spaced { letter-spacing: 5px; }
  .icon { fill: none; stroke: #6a6a6a; stroke-width: 2; stroke-linecap: round; stroke-linejoin: round; }
  .connector { stroke: var(--node); stroke-width: 5; fill: none; }
  .legend-heading { font-size: 20px; font-weight: 600; fill: #666; letter-spacing: 0.8px; }
  .legend-text { font-size: 19px; font-weight: 400; }
</style>
</head>
<body>
<svg class="process-chart" viewBox="0 0 1200 1200" xmlns="http://www.w3.org/2000/svg">
  <text class="title" x="600" y="73" text-anchor="middle">Space For Title</text>

  <!-- Roles -->
  <g class="roles">
    <text class="role-label role-school" x="600" y="154" text-anchor="middle">SCHOOL</text>
    <circle cx="600" cy="200" r="21" fill="var(--school)"/>

    <text class="role-label role-arch" x="432" y="229" text-anchor="middle">ARCHITECTURAL</text>
    <text class="role-label role-arch" x="432" y="255" text-anchor="middle">CONSULTANT</text>
    <circle cx="432" cy="292" r="21" fill="var(--arch)"/>

    <text class="role-label role-fund" x="767" y="229" text-anchor="middle">FUNDRAISING</text>
    <text class="role-label role-fund" x="767" y="255" text-anchor="middle">CONSULTANT</text>
    <circle cx="768" cy="292" r="21" fill="var(--fund)"/>
  </g>

  <!-- Merging bands -->
  <g class="merge-arrow">
    <path d="M592 235 L600 242 L608 235 L608 335 L592 335 Z" fill="#74d7dc"/>
    <path d="M465 284 L577 284 Q592 284 592 299 L592 335 L578 335 L578 304 Q578 300 574 300 L465 300 L472 292 Z" fill="var(--arch-band)"/>
    <path d="M735 284 L623 284 Q608 284 608 299 L608 335 L622 335 L622 304 Q622 300 626 300 L735 300 L728 292 Z" fill="var(--fund-bright)"/>
    <polygon points="563,330 613,330 588,362" fill="var(--arch-band)" opacity="0.85"/>
    <polygon points="587,330 637,330 612,362" fill="var(--fund-bright)" opacity="0.85"/>
    <polygon points="575,340 625,340 600,377" fill="#74d7dc" opacity="0.85"/>
  </g>

  <!-- Connectors -->
  <polyline class="connector" points="600,438 554,520 600,594 646,520 600,438"/>
  <line class="connector" x1="600" y1="594" x2="600" y2="915"/>

  <!-- Nodes -->
  <g class="nodes">
    <g class="node shared" transform="translate(600 438)">
      <circle r="35" fill="#fff" stroke="#c9c9c9" stroke-width="2"/>
      <circle r="30" fill="var(--node)"/>
      <circle cx="0" cy="-13" r="10" fill="var(--school-bright)"/>
      <circle cx="-11" cy="7" r="10" fill="var(--arch-dot)"/>
      <circle cx="11" cy="7" r="10" fill="var(--fund-bright)"/>
    </g>
    <g class="node arch" transform="translate(554 520)"><circle r="26" fill="var(--node)"/><circle r="10" fill="var(--arch-dot)"/></g>
    <g class="node arch" transform="translate(646 520)"><circle r="26" fill="var(--node)"/><circle r="10" fill="var(--arch-dot)"/></g>
    <g class="node arch" transform="translate(600 594)"><circle r="26" fill="var(--node)"/><circle r="10" fill="var(--arch-dot)"/></g>
    <g class="node arch" transform="translate(600 668)"><circle r="26" fill="var(--node)"/><circle r="10" fill="var(--arch-dot)"/></g>
    <g class="node shared" transform="translate(600 750)">
      <circle r="35" fill="#fff" stroke="#c9c9c9" stroke-width="2"/>
      <circle r="30" fill="var(--node)"/>
      <circle cx="0" cy="-13" r="10" fill="var(--school-bright)"/>
      <circle cx="-11" cy="7" r="10" fill="var(--arch-dot)"/>
      <circle cx="11" cy="7" r="10" fill="var(--fund-bright)"/>
    </g>
    <g class="node arch" transform="translate(600 831)"><circle r="26" fill="var(--node)"/><circle r="10" fill="var(--arch-dot)"/></g>
    <g class="node shared" transform="translate(600 915)">
      <circle r="35" fill="#fff" stroke="#c9c9c9" stroke-width="2"/>
      <circle r="30" fill="var(--node)"/>
      <circle cx="0" cy="-13" r="10" fill="var(--school-bright)"/>
      <circle cx="-11" cy="7" r="10" fill="var(--arch-dot)"/>
      <circle cx="11" cy="7" r="10" fill="var(--fund-bright)"/>
    </g>
  </g>

  <!-- Right steps -->
  <g class="step visioning">
    <g class="icon" transform="translate(722 438)">
      <path d="M-34 0 Q0 -28 34 0 Q0 28 -34 0 Z"/>
      <circle r="12"/>
      <circle r="4"/>
      <path d="M-5 12 L-5 20 L5 20 L5 12"/>
      <path d="M0 -22 V-27 M-14 -19 L-17 -24 M14 -19 L17 -24 M-26 -12 L-30 -16 M26 -12 L30 -16"/>
    </g>
    <text class="step-label" x="769" y="445">VISIONING</text>
  </g>

  <g class="step space-needs">
    <g class="icon" transform="translate(722 520)">
      <rect x="-21" y="-21" width="42" height="42" rx="4"/>
      <path d="M0 -21 V-8 Q6 -8 6 -3 Q6 2 0 2 V21 M-21 0 H-8 Q-8 -6 -3 -6 Q2 -6 2 0 H21"/>
    </g>
    <text class="step-label" x="769" y="501">SPACE</text>
    <text class="step-label spaced" x="769" y="526">NEEDS</text>
    <text class="step-label" x="769" y="552">ASSESSMENT</text>
  </g>

  <g class="step problem-defined">
    <g class="icon" transform="translate(722 605)">
      <path d="M-20 -25 H20 Q22 -25 22 -23 V17 Q22 19 20 19 H6 L0 30 L-6 19 H-20 Q-22 19 -22 17 V-23 Q-22 -25 -20 -25 Z"/>
      <path d="M0 -17 V3"/>
      <circle cx="0" cy="11" r="1.5" fill="#6a6a6a"/>
    </g>
    <text class="step-label" x="768" y="611">PROBLEM DEFINED</text>
  </g>

  <g class="step assess-select">
    <g class="icon" transform="translate(722 750)">
      <rect x="-21" y="-32" width="42" height="64" rx="2"/>
      <rect x="-14" y="-24" width="11" height="11"/>
      <path d="M-12 -19 L-9 -15 L-2 -25 M2 -18 H14"/>
      <rect x="-14" y="-6" width="11" height="11"/>
      <path d="M-12 -1 L-9 3 L-2 -7 M2 0 H14"/>
      <path d="M-21 28 L10 14 L21 24"/>
    </g>
    <text class="step-label" x="769" y="758">ASSESS &amp; SELECT</text>
  </g>

  <g class="step implement">
    <g class="icon" transform="translate(722 910)">
      <path d="M28 -28 Q2 -26 -10 2 L2 14 Q30 2 28 -28 Z"/>
      <circle cx="8" cy="-8" r="5"/>
      <path d="M-8 -2 L-20 -2 L-12 -12 L-2 -12 M8 12 L8 24 L18 16 L18 6"/>
      <path d="M-12 10 Q-24 12 -26 26 Q-12 24 -10 12"/>
    </g>
    <text class="step-label" x="768" y="922">IMPLEMENT PLAN !</text>
  </g>

  <!-- Left steps -->
  <g class="step physical-conditions">
    <text class="step-label" x="450" y="505" text-anchor="end">PHYSICAL</text>
    <text class="step-label" x="450" y="530" text-anchor="end">CONDITIONS</text>
    <text class="step-label" x="450" y="556" text-anchor="end">ASSESSMENT</text>
    <g class="icon" transform="translate(490 520)">
      <path d="M-8 -24 V-34 H22 V16"/>
      <path d="M-22 18 V-18 H2 V-4"/>
      <path d="M-16 -12 H-12 M-8 -12 H-4 M-16 -6 H-12 M-8 -6 H-4 M-16 0 H-12 M-16 6 H-12 M2 -28 H6 M12 -28 H16 M12 -22 H16 M12 -16 H16 M12 -10 H16"/>
      <circle cx="4" cy="10" r="9"/>
      <path d="M10 17 L20 27"/>
    </g>
  </g>

  <g class="step identify-solutions">
    <text class="step-label" x="453" y="682" text-anchor="end">IDENTIFY SOLUTIONS</text>
    <g class="icon" transform="translate(490 668)">
      <path d="M-14 32 V20 Q-28 8 -26 -10 Q-22 -34 2 -34 Q24 -32 26 -10 L30 2 L24 4 V14 Q24 20 16 20 L10 20 V32"/>
      <circle cx="0" cy="-10" r="9"/>
      <path d="M-4 -1 V6 H4 V-1 M-3 9 H3 M0 -26 V-23 M-13 -21 L-11 -19 M13 -21 L11 -19"/>
    </g>
  </g>

  <g class="step compile-report">
    <text class="step-label" x="453" y="832" text-anchor="end">COMPILE REPORT</text>
    <g class="icon" transform="translate(490 831)">
      <path d="M-22 16 V-30 H4"/>
      <path d="M-16 22 V-24 H10"/>
      <path d="M-10 28 V-18 H12 L24 -6 V28 Z M12 -18 V-6 H24"/>
      <path d="M-3 2 H16 M-3 10 H16 M-3 18 H16"/>
    </g>
  </g>

  <!-- Legend -->
  <g class="legend">
    <text class="legend-heading" x="250" y="1052">Areas of responsibility colors meaning:</text>
    <circle cx="258" cy="1087" r="8" fill="var(--school)"/>
    <text class="legend-text role-school" x="281" y="1094">BLUE</text>
    <text class="legend-text role-school" x="391" y="1094">: SCHOOL</text>
    <circle cx="258" cy="1119" r="8" fill="var(--arch)"/>
    <text class="legend-text role-arch" x="281" y="1126">RED</text>
    <text class="legend-text role-arch" x="391" y="1126">: ARCHITECTURAL CONSULTANT</text>
    <circle cx="258" cy="1150" r="8" fill="var(--fund)"/>
    <text class="legend-text role-fund" x="281" y="1157">GREEN</text>
    <text class="legend-text role-fund" x="391" y="1157">: FUNDRAISING CONSULTANT</text>
  </g>
</svg>
</body>
</html>
```